Fruits and Vegetables distribution company needs a new eye catching website

We need to get our website up to date. Our clients will look at our website to learn about our products and services. Our design needs to be simple yet impactful to make our brand memorable to our visitors. We need to have somewhere to tell our clients about our history, products and services, our team. We can throw in a few fun facts and figures and maybe some testimonials to impress. We have 4 theme colors that we want to incorporate into the design, you can get in touch for the HEX/RGB codes. Please remember that smooth operation of any animations and interactions is very important.

Need extra days to review

```html
<!DOCTYPE html>
<html lang="en">
<head>
<meta charset="utf-8">
<title>Sunvale — Fresh Food</title>
<link href="https://fonts.googleapis.com/css2?family=Montserrat:wght@300;400;500;600;700&family=Dancing+Script:wght@600&family=Caveat:wght@500&display=swap" rel="stylesheet">
<style>
:root{
  --green:#8cc63f;
  --green-dark:#6fa82a;
  --orange:#f5a623;
  --text:#4a4a4a;
  --muted:#9a9a9a;
  --line:#d8d8d8;
  --paper:#f3f3f3;
  --slate:#9ca5b4;
  --white:#ffffff;
  --kraft:#c9a46a;
  --pink:#f2a9bf;
  --leaf:#b9d66b;
}
*{box-sizing:border-box;margin:0;padding:0}
html,body{width:1200px;height:3822px;overflow:hidden}
body{position:relative;background:var(--white);font-family:"Montserrat",sans-serif;color:var(--text)}
.abs{position:absolute}
.page{position:absolute;left:46px;top:46px;width:1108px;height:3725px;background:var(--paper);box-shadow:0 0 8px rgba(0,0,0,.12);overflow:hidden}
.wood{background:var(--paper) repeating-linear-gradient(180deg,transparent 0 118px,rgba(0,0,0,.04) 118px 120px)}
.script{font-family:"Dancing Script",cursive;font-weight:600;color:var(--text)}
.ph{position:absolute}
.pack{position:absolute;border-radius:3px;box-shadow:0 3px 6px rgba(0,0,0,.2)}
.pack.green{background:linear-gradient(180deg,var(--kraft) 0 35%,var(--leaf) 35% 100%)}
.pack.pink{background:linear-gradient(180deg,var(--kraft) 0 35%,var(--pink) 35% 100%)}
.pack.yellow{background:linear-gradient(180deg,var(--kraft) 0 35%,#e6d27a 35% 100%)}
.pill{position:absolute;border:1px solid #bdbdbd;border-radius:30px;text-align:center;color:var(--text);font-size:11px;letter-spacing:.5px;text-transform:uppercase;background:var(--white)}

/* nav */
.nav{position:absolute;left:0;top:0;width:1108px;height:61px;background:var(--white)}
.nav a{position:absolute;top:24px;font-size:12px;color:var(--text);text-decoration:none}
.nav a.active{color:var(--orange)}
.nav .active-bar{position:absolute;left:260px;top:0;width:62px;height:4px;background:var(--orange)}
.brand{position:absolute;left:524px;top:8px;width:60px;height:60px;background:var(--white);box-shadow:0 2px 6px rgba(0,0,0,.15);display:flex;flex-direction:column;align-items:center;justify-content:center;gap:4px}
.brand i{width:14px;height:14px;border-radius:50%;background:var(--orange)}
.brand span{font-size:10px;font-weight:600;color:var(--text)}
.cart b{font-weight:700}
.cart small{display:block;color:var(--orange);font-size:9px;text-align:right}

/* hero */
.hero-title{left:0;width:1108px;top:124px;text-align:center;font-size:32px;font-weight:600;letter-spacing:2px;color:#9aa3ad;line-height:38px;text-transform:uppercase}
.hero-sub{left:0;width:1108px;top:206px;text-align:center;font-size:15px;color:var(--muted);line-height:21px}
.hero-note{left:135px;top:283px;font-family:"Caveat",cursive;font-size:22px;color:var(--green);line-height:22px;transform:rotate(-6deg)}
.hero-price{left:402px;top:286px;font-family:"Caveat",cursive;font-size:30px;color:var(--orange)}
.section-title{left:0;width:1108px;text-align:center;font-size:38px}

.about-text{left:148px;width:420px;font-size:12.5px;line-height:21px;color:var(--text)}
.frame{position:absolute;background:#e7e7e7;border:5px solid var(--white);box-shadow:0 3px 8px rgba(0,0,0,.25)}

.process{left:0;top:1057px;width:1108px;height:286px;background:var(--slate);color:var(--white);text-align:center}
.process h2{margin-top:60px;font-size:27px;font-weight:400}
.process p{width:780px;margin:18px auto 0;font-size:12.5px;font-weight:600;line-height:22px}
.process .more{margin-top:10px;color:var(--green);font-size:10px;font-weight:600}

.card{position:absolute;top:1597px;height:242px;background:var(--white);box-shadow:0 2px 10px rgba(0,0,0,.18);text-align:center}
.card .price{margin-top:92px;color:var(--green);font-size:19px}
.card .desc{margin-top:6px;font-size:17px;line-height:22px;color:var(--text)}
.btn-green{position:absolute;left:484px;top:1893px;width:140px;height:38px;border-radius:20px;background:var(--green);color:var(--white);font-size:11px;font-weight:700;text-align:center;line-height:38px}

.testi-photo{position:absolute;top:2094px;height:115px;background:#c8a98d;border:4px solid var(--white);box-shadow:0 2px 6px rgba(0,0,0,.25)}
.testi-name{position:absolute;top:2214px;font-size:11px;font-weight:600;color:var(--muted)}
.dots span{display:inline-block;width:8px;height:8px;border-radius:50%;background:#d0d0d0;margin:0 3px}
.dots span.on{background:var(--orange)}

.smart{left:0;top:2400px;width:1108px;height:484px;background:var(--white);box-shadow:0 0 10px rgba(0,0,0,.1)}
.article{position:absolute;top:2509px;width:255px;height:312px;background:var(--white);box-shadow:0 1px 6px rgba(0,0,0,.18)}
.article .img{height:160px}
.article h3{margin:14px 12px 6px;font-size:12px;font-weight:600}
.article p{margin:0 12px;font-size:10px;line-height:14px}
.article .read{margin:8px 12px;font-size:10px;color:var(--green-dark);font-weight:600}
.round{position:absolute;top:2646px;width:28px;height:28px;border-radius:50%;border:1px solid #cfcfcf;background:var(--white)}

.news{left:0;top:2884px;width:1108px;height:306px;background:#f6f6f6}
.input{position:absolute;left:298px;top:3057px;width:502px;height:57px;background:var(--white);border-radius:30px;box-shadow:0 2px 8px rgba(0,0,0,.15);font-size:13px;color:var(--muted);line-height:57px;padding-left:30px}

.footer{left:0;top:3190px;width:1108px;height:535px;background:var(--slate);color:var(--white)}
.field{position:absolute;border-bottom:1px solid rgba(255,255,255,.7);font-size:11px;font-weight:600;padding-bottom:8px}
.col{position:absolute;top:3585px;font-size:9.5px;line-height:14px}
.col h4{font-size:11px;font-weight:700;margin-bottom:4px}
</style>
</head>
<body>
<div class="page wood">

  <!-- navigation -->
  <nav class="nav">
    <div class="active-bar"></div>
    <a style="left:176px">About us</a>
    <a class="active" style="left:264px">Contact us</a>
    <a style="left:366px">Our Products</a>
    <div class="brand"><i></i><span>Sunvale</span></div>
    <a style="left:668px">Online Shopping</a>
    <a style="left:795px">Login</a>
    <a class="cart" style="left:864px;top:20px"><b>Shopping cart</b><small>0 items</small></a>
  </nav>

  <!-- hero -->
  <div class="ph" role="img" aria-label="Lemon slice decoration" style="left:-30px;top:-20px;width:90px;height:70px;border-radius:50%;background:#f4de5c"></div>
  <div class="ph" role="img" aria-label="Green apple" style="left:914px;top:148px;width:86px;height:86px;border-radius:50%;background:radial-gradient(circle at 40% 40%,#a6d94d,#5e9d1f)"></div>
  <h1 class="abs hero-title">Delicious food<br>with trully fresh ingredients</h1>
  <p class="abs hero-sub">Only fresh and delicious food for you and your family with amazing<br>strength and energy injection</p>
  <div class="abs hero-note">Only Fresh<br>Products!</div>
  <svg class="abs" style="left:232px;top:300px" width="90" height="36" viewBox="0 0 90 36"><path d="M2 8 C30 30 60 30 84 20" fill="none" stroke="#8a8a8a" stroke-width="1.5"/><path d="M76 14 L85 20 L76 26" fill="none" stroke="#8a8a8a" stroke-width="1.5"/></svg>
  <div class="abs hero-price">From $2.99</div>
  <div class="pill" style="left:529px;top:286px;width:160px;height:44px;line-height:42px;font-size:13px;border-radius:22px">Buy now</div>
  <div class="pack green" role="img" aria-label="Pancake mix pack" style="left:328px;top:370px;width:104px;height:150px"></div>
  <div class="pack pink" role="img" aria-label="Pancake mix pack" style="left:446px;top:362px;width:104px;height:158px"></div>
  <div class="pack green" role="img" aria-label="Pancake mix pack" style="left:561px;top:366px;width:104px;height:154px"></div>
  <div class="pack yellow" role="img" aria-label="Pancake mix pack" style="left:676px;top:362px;width:104px;height:158px"></div>

  <!-- about -->
  <h2 class="abs script" style="left:148px;top:644px;font-size:34px">About us!</h2>
  <p class="abs about-text" style="top:714px">Lorem ipsum dolor sit amet, consectetuer adipiscing elit. Aenean commodo ligula eget dolor. Aenean massa. Cum sociis natoque penatibus et magnis dis parturient montes, nascetur ridiculus mus. Donec quam felis, ultricies nec, pellentesque eu, pretium quis, sem. Nulla consequat massa quis enim. Donec pede justo, fringilla vel, aliquet nec, vulputate eget, arcu.</p>
  <p class="abs about-text" style="top:876px">Lorem ipsum dolor sit amet, consectetuer adipiscing elit. Aenean commodo ligula eget dolor. Aenean massa. Cum sociis natoque penatibus et magnis.</p>
  <div class="frame" role="img" aria-label="Shop interior with shelves" style="left:629px;top:711px;width:165px;height:173px;background:#a8523a"></div>
  <div class="frame" role="img" aria-label="Grocery store aisle" style="left:782px;top:647px;width:178px;height:173px;background:#7a5b4a"></div>
  <div class="frame" role="img" aria-label="Jars of preserves" style="left:787px;top:838px;width:168px;height:122px;background:#d8c6a5"></div>

  <!-- process -->
  <section class="abs process" role="img" aria-label="Process of making background" style="">
    <h2>The Process of Making</h2>
    <p>Lorem ipsum dolor sit amet, consectetuer adipiscing elit. Aenean commodo ligula eget dolor. Aenean massa. Cum sociis natoque penatibus et magnis dis parturient montes, nascetur ridiculus mus. Donec quam felis, ultricies nec, pellentesque eu, pretium quis, sem. Nulla consequat</p>
    <div class="more">Read more</div>
  </section>

  <!-- selected products -->
  <div class="ph" role="img" aria-label="Strawberry" style="left:85px;top:1400px;width:34px;height:40px;border-radius:45% 45% 50% 50%;background:#d9282f"></div>
  <div class="ph" role="img" aria-label="Lemon" style="left:976px;top:1492px;width:90px;height:72px;border-radius:50%;background:#f3d83a"></div>
  <div class="ph" role="img" aria-label="Lemon" style="left:96px;top:1800px;width:70px;height:56px;border-radius:50%;background:#f3d83a"></div>
  <h2 class="abs script section-title" style="top:1414px">Selected products</h2>

  <div class="card" style="left:114px;width:230px"><div class="price">$7.99</div><div class="desc">Your choice what text<br>to write here</div><div class="pill" style="left:52px;top:178px;width:126px;height:30px;line-height:28px;font-size:9px">Buy now</div></div>
  <div class="card" style="left:433px;width:255px"><div class="price">$19.99</div><div class="desc">Your choice what text<br>to write here</div><div class="pill" style="left:64px;top:178px;width:126px;height:30px;line-height:28px;font-size:9px">Buy now</div></div>
  <div class="card" style="left:802px;width:242px"><div class="price">$12.99</div><div class="desc">Your choice what text<br>to write here</div><div class="pill" style="left:58px;top:178px;width:126px;height:30px;line-height:28px;font-size:9px">Buy now</div></div>

  <div class="pack green" role="img" aria-label="Pancake mix pack" style="left:190px;top:1486px;width:80px;height:150px"></div>
  <div class="pack green" role="img" aria-label="Pancake mix pack" style="left:470px;top:1508px;width:72px;height:128px"></div>
  <div class="pack green" role="img" aria-label="Pancake mix pack" style="left:580px;top:1508px;width:72px;height:128px"></div>
  <div class="pack pink" role="img" aria-label="Pancake mix pack" style="left:520px;top:1492px;width:80px;height:146px"></div>
  <div class="pack green" role="img" aria-label="Pancake mix pack" style="left:830px;top:1500px;width:80px;height:138px"></div>
  <div class="pack pink" role="img" aria-label="Pancake mix pack" style="left:898px;top:1494px;width:84px;height:144px"></div>
  <div class="btn-green">SHOW ALL</div>

  <!-- testimonials -->
  <div class="abs" style="left:0;top:1966px;width:1108px;height:1px;background:var(--line)"></div>
  <h2 class="abs script section-title" style="top:2016px;font-size:34px">Testimonials</h2>
  <div class="abs" style="left:0;top:2124px;width:1108px;height:1px;background:var(--line)"></div>
  <div class="abs" style="left:247px;top:2133px;font-size:14px;color:var(--orange);font-weight:500">
    <svg width="26" height="14" viewBox="0 0 26 14" style="vertical-align:-2px"><path d="M25 7H3M9 1L2 7l7 6" fill="none" stroke="#f5a623" stroke-width="2.5"/></svg> Previous</div>
  <div class="abs" style="left:751px;top:2133px;font-size:14px;color:#bdbdbd">Next one
    <svg width="26" height="14" viewBox="0 0 26 14" style="vertical-align:-2px"><path d="M1 7h22M17 1l7 6-7 6" fill="none" stroke="#bdbdbd" stroke-width="2"/></svg></div>
  <div class="testi-photo" role="img" aria-label="Customer portrait" style="left:413px;width:132px"></div>
  <div class="testi-photo" role="img" aria-label="Customer portrait" style="left:571px;width:127px;background:#8a4a38"></div>
  <div class="testi-name" style="left:440px">Nora Vell</div>
  <div class="testi-name" style="left:606px">Leo Brant</div>
  <p class="abs" style="left:150px;width:808px;top:2244px;text-align:center;font-size:12.5px;line-height:22px">Lorem ipsum dolor sit amet, consectetuer adipiscing elit. Aenean commodo ligula eget dolor. Aenean massa. Cum sociis natoque penatibus et magnis dis parturient montes, nascetur ridiculus mus. Donec quam felis, ultricies nec, pellentesque eu, pretium quis, sem. Nulla consequat massa quis enim. Donec pede justo, fringilla vel, aliquet nec, vulputate eget, arcu. In enim justo, rhoncus ut,</p>
  <div class="abs dots" style="left:0;width:1108px;top:2356px;text-align:center"><span></span><span class="on"></span><span></span><span></span><span></span><span></span></div>

  <!-- get smarter -->
  <section class="abs smart"></section>
  <h2 class="abs script section-title" style="top:2444px;font-size:34px">Get smarter</h2>
  <div class="round" style="left:65px"><svg width="26" height="26" viewBox="0 0 26 26"><path d="M15 8l-5 5 5 5" fill="none" stroke="#999" stroke-width="1.5"/></svg></div>
  <div class="round" style="left:1013px"><svg width="26" height="26" viewBox="0 0 26 26"><path d="M11 8l5 5-5 5" fill="none" stroke="#999" stroke-width="1.5"/></svg></div>
  <article class="article" style="left:153px"><div class="img" role="img" aria-label="Fresh fruit stall" style="background:#7d6a3c"></div><h3>Title of the Arcticle</h3><p>Lorem ipsum dolor sit amet consectetuer adipiscing elit. Aenean commodo ligula eget dolor. Aenean massa. Cum sociis natoque penatibus et magnis dis parturient montes.</p><div class="read">Read More</div></article>
  <article class="article" style="left:430px"><div class="img" role="img" aria-label="Bowl of noodle soup" style="background:#e0a65a"></div><h3>Title of the Arcticle</h3><p>Lorem ipsum dolor sit amet consectetuer adipiscing elit. Aenean commodo ligula eget dolor. Aenean massa. Cum sociis natoque penatibus et magnis dis parturient montes.</p><div class="read">Read More</div></article>
  <article class="article" style="left:708px"><div class="img" role="img" aria-label="Team meeting at a table" style="background:#8ea2b4"></div><h3>Title of the Arcticle</h3><p>Lorem ipsum dolor sit amet consectetuer adipiscing elit. Aenean commodo ligula eget dolor. Aenean massa. Cum sociis natoque penatibus et magnis dis parturient montes.</p><div class="read">Read More</div></article>

  <!-- newsletter -->
  <section class="abs news"></section>
  <h2 class="abs" style="left:0;width:1108px;top:2944px;text-align:center;font-size:24px;font-weight:400">Subscribe to our newsletter</h2>
  <p class="abs" style="left:0;width:1108px;top:2988px;text-align:center;font-size:14px;color:var(--muted);line-height:19px">Lorem ipsum dolor sit amet, consec<br>scing elit commodo ligula</p>
  <div class="input">Your email address here...</div>
  <svg class="abs" style="left:746px;top:3077px" width="28" height="18" viewBox="0 0 28 18"><rect width="28" height="18" rx="2" fill="#d9302f"/><path d="M1 1l13 9 13-9" fill="none" stroke="#fff" stroke-width="1.5"/></svg>
  <div class="pack green" role="img" aria-label="Pancake mix pack" style="left:43px;top:3087px;width:56px;height:110px;z-index:2"></div>
  <div class="pack pink" role="img" aria-label="Pancake mix pack" style="left:86px;top:3067px;width:62px;height:130px;z-index:3"></div>
  <div class="pack green" role="img" aria-label="Pancake mix pack" style="left:140px;top:3087px;width:56px;height:110px;z-index:2"></div>

  <!-- footer -->
  <footer class="abs footer" role="img" aria-label="Faded pancake mix pack background">
  </footer>
  <h2 class="abs script" style="left:0;width:1108px;top:3254px;text-align:center;font-size:34px;color:var(--white)">Get in touch</h2>
  <div class="field" style="left:227px;top:3341px;width:313px;color:#fff">Your Full Name...</div>
  <div class="field" style="left:565px;top:3341px;width:319px;color:#fff">Your Email Address...</div>
  <div class="field" style="left:227px;top:3400px;width:657px;color:#fff">Write a message for us...</div>
  <div class="abs" style="left:227px;top:3459px;width:13px;height:13px;background:#fff"></div>
  <div class="abs" style="left:248px;top:3459px;font-size:10px;color:#fff">Remember me</div>
  <div class="abs" style="left:666px;top:3455px;width:80px;font-size:8px;line-height:10px;color:#fff">We will answer<br>in 24 hours</div>
  <div class="abs" style="left:751px;top:3450px;width:135px;height:33px;border:1px solid #fff;color:#fff;font-size:10px;font-weight:700;text-align:center;line-height:31px">SEND A MESSAGE</div>

  <div class="abs" style="left:201px;top:3585px;width:84px;text-align:center;color:#fff">
    <div style="width:22px;height:22px;border-radius:50%;background:#fff;margin:0 auto 8px"></div>
    <div style="font-size:15px;font-weight:600;letter-spacing:1px">SUNVALE</div>
  </div>
  <div class="col" style="left:354px;color:#fff"><h4>Navigation</h4>How it Works<br>Pricing Page<br>Try Our Foods<br>Sign Up<br>Login</div>
  <div class="col" style="left:507px;color:#fff"><h4>Policy</h4>Conditions &amp; Terms<br>About us<br>Privacy Policy<br>Write to us<br>Data Security</div>
  <div class="col" style="left:683px;color:#fff"><h4>Contacts</h4>Your Street Adress<br>Phone Numbers<br>Email Addresses<br>Working Hours<br>Feedback</div>
  <div class="col" style="left:856px;color:#fff"><h4>Social</h4>Community<br>Circle<br>Updates</div>
</div>
</body>
</html>
```